Shipping and Logistics, Project

Project description : Company Profile

A total logistics company covering domestic / international freight forwarding, warehouse management services, haulage, supply chain management, transport management & distribution, procurement & assembly services, shipping, chartering & bunker services, project logistics & tax exemption consultancy, oil & gas logistics, halal logistics services & integrated logistics management. We’re a well-established and experienced freight forwarder in Kuala Lumpur, Malaysia. We specialize in customized value-added solution that optimizes your supply chain by trimming inventory, reducing logistics cost and enhancing your customer service levels.

As a member of the Continental Parcel and Carriage Alliance which comprise of 170 global freight agents in 80 countries that promotes great handling in cross-trade logistics and freighting. You could rely on our efficiency in handlings of export cargo (FCL, LCL, Bulk and Conventional) between our global network offices worldwide with a total scale of 10,000 groomed specialists in various logistics division working together to ensure delivery task meets with your expectation. With our dedicated qualified and experienced professionals, we are fully committed to serving our clients.

Our generic services are listed below for your reference:

• Air Freight
• Ocean Freight FCL & LCL
• Container Haulage
• Warehousing
• Transportation and Distribution within Malaysia and Thailand
• Cross-Border Road Line-hauls between Thailand, Malaysia, Singapore and Laos
• Customs Brokerage and Forwarding
• Project Cargo Freight Forwarding for setting up of new plants / factories and ad hoc heavy-lift
• Air-Sea-Road-Rail multi-modal options
• Import / Export / Storage / Documentation / Handling of DG / Hazmat
• Vessel and Aircraft Charters

Our Mission
Based on the motto “Quick, Reliable and Polite”, we are dedicated to upholding the following three points corporate philosophy:
1. Adhering to the principle that “the customer always comes first”.
2. Contributing to the development of the local community.
3. Making it our duty to be responsible and sincere.

Our Edge
• One-Stop Logistics Solutions
• Extensive Network Throughout Malaysia
• Highly Qualified and Experienced Pool of Professionals
• Comprehensive IT Solutions
• Innovative and Customer-focused Solutions
• Flexible and Consistent in Managing Exceptions
• Total Supply Chain Visibility

Target Market
1. We sell the logistics services to all the industry in Malaysia and Worldwide. (ONE Stop Logistics Solutions)

Competitor
1. RT Vollmark
2. Corventa Transport
3. Brastow + Feld
4. TOLRI
5. QVN
6. Trundelles
7. Wiro Logistics

Rules for Picking a Company Name
1. Unique and unforgettable
2. Avoid unusual spellings
3. Easy to pronounce and remember
4. Keep it simple
5. Make some sense
6. Give a clue

Rules for Picking a Company Logo
4. Keep it simple
5. Make some sense
6. Give a clue

1. Simplicity
2. Memorability
3. Originality
4. Modern Yet Timeless
5. Balance
6. Complementary
7. Versatility

Stationery Information
1. Company Name : Tenhaul Solutions Sdn Bhd
2. Company Registration : 2738516-P
3. Address : 42-07, Jalan Seri Dedap 5, Taman Bukit Kenari, 81100 Johor Bahru, Johor, Malaysia.
4. Name : Derek Tan
5. Position : Manager
6. Mobile No : (+6019) 4183907
7. Office No : (+607) 2918476
8. Fax No : Not Available
9. Email Address : derek.tan@tenhaul-solutions.example
10. Web Domain : www.tenhaul-solutions.example
11. Company Slogan : Be Globally Connected

Target Market(s)

Corporate Company

Industry/Entity Type

Shipping and Logistics Industry

Requirements
Must have
• Company Full Name : TENHAUL SOLUTIONS SDN. BHD.
Nice to have
• Keep it simple and unforgettable ...

```html
<!DOCTYPE html>
<html lang="en">
<head>
<meta charset="utf-8">
<title>Tenhaul Solutions – Company Profile</title>
<link href="https://fonts.googleapis.com/css2?family=Montserrat:wght@400;500;600;700;800&display=swap" rel="stylesheet">
<style>
:root{
  --bg:#a7a8ac;
  --paper:#ffffff;
  --blue:#2f86d9;
  --blue-deep:#1d6fc2;
  --ink:#1f2126;
  --text:#55585e;
  --rule:#9aa0a8;
  --dark:#121418;
}
*{margin:0;padding:0;box-sizing:border-box}
html,body{width:1200px;height:1153px;overflow:hidden;background:var(--bg)}
body{position:relative;font-family:'Montserrat',sans-serif;color:var(--text)}
.page{position:absolute;background:var(--paper);overflow:hidden}
.abs{position:absolute}
.photo{position:absolute}
.blue{color:var(--blue)}
.ink{color:var(--ink)}

/* brand wordmark */
.brand{position:absolute;display:flex;align-items:center;gap:8px;font-weight:700;color:var(--blue);letter-spacing:.5px;line-height:1}
.brand .mark{background:var(--blue);display:block}

/* section headings with rule */
.heading{position:absolute;font-weight:700;color:var(--ink);line-height:1}
.heading span{color:var(--blue)}
.rule{position:absolute;height:1px;background:var(--rule)}
.rule i{position:absolute;left:0;top:-1.5px;height:4px;background:var(--blue)}

/* cover */
.cover .company{left:23px;top:392px;font-size:20px;line-height:1;font-weight:400;color:var(--ink);letter-spacing:.5px}
.cover .profile{left:22px;top:409px;font-size:37px;line-height:1;font-weight:800;color:var(--blue);letter-spacing:.5px}
.cover .underline{left:24px;top:448px;width:91px;height:4px;background:var(--blue)}
.web{position:absolute;font-size:10px;line-height:1;letter-spacing:3px;color:var(--ink);white-space:nowrap}
.web b{font-weight:500;color:var(--blue)}

/* body copy */
.copy{position:absolute;font-size:6.6px;line-height:9.8px;text-align:justify;color:var(--text)}
.services{position:absolute;font-size:6.6px;line-height:9.8px;list-style:none}
.services li{position:relative;padding-left:14px}
.services li::before{content:"";position:absolute;left:6px;top:4px;width:2.5px;height:2.5px;border-radius:50%;background:var(--blue)}

/* footer */
.foot{position:absolute;left:0;right:0;top:474px;height:1px;background:var(--blue)}
.pgno{position:absolute;top:470px;width:9px;height:8px;background:var(--blue);color:#fff;font-size:5px;line-height:8px;text-align:center;font-weight:600}

/* mission */
.mission-box{position:absolute;top:125px;width:84px;height:104px;background:var(--blue);color:#fff;font-size:7px;line-height:9.8px;font-weight:500;text-align:center;padding:30px 4px 0}
.badge{position:absolute;top:-19px;left:50%;transform:translateX(-50%);width:42px;height:46px}
.badge b{position:absolute;inset:0;display:flex;align-items:center;justify-content:center;font-size:18px;font-weight:800;color:#fff}

/* edge */
.edge{position:absolute;left:0;top:249px;width:343px;height:207px;background:linear-gradient(135deg,#1a1c22 0%,#0e1014 60%,#232730 100%)}
.edge .heading{color:#fff}
.edge-item{position:absolute;width:86px;text-align:center;color:#fff;font-size:6px;line-height:7.2px;font-weight:600}
.edge-item svg{display:block;margin:0 auto 4px;width:30px;height:33px}

/* spread 2 */
.sub{position:absolute;font-size:12px;font-weight:700;color:var(--ink)}
.small{position:absolute;font-size:7.8px;line-height:10px;color:var(--text)}
.numlist{position:absolute;list-style:none;font-size:7.8px;color:var(--text)}
.numlist li{height:15.2px;display:flex;align-items:center;gap:3px}
.dot{display:inline-flex;width:7px;height:7px;border-radius:50%;background:var(--blue);color:#fff;font-size:5px;font-weight:700;align-items:center;justify-content:center}
.num{color:var(--blue);font-weight:700}

/* back cover */
.back .title{position:absolute;left:0;right:0;top:63px;text-align:center;font-size:17px;font-weight:700;color:var(--blue);letter-spacing:-.2px}
.lined{position:absolute;left:0;right:0;display:flex;align-items:center;gap:4px;color:var(--ink);font-size:7.6px;font-weight:500;white-space:nowrap}
.lined::before,.lined::after{content:"";flex:1;height:1px;background:var(--ink)}
.back .person{position:absolute;left:0;right:0;top:350px;text-align:center;font-size:19px;font-weight:500;color:var(--ink)}
.contact{position:absolute;left:0;right:0;top:382px;height:65px;background:var(--blue);color:#fff;font-size:7.4px;line-height:9.8px;text-align:center;padding-top:9px}
</style>
</head>
<body>

<!-- Front cover -->
<section class="page cover" style="left:56px;top:56px;width:342px;height:484px">
  <div class="brand" style="left:24px;top:42px;font-size:17px">
    <span class="mark" style="width:14px;height:14px"></span>TENHAUL SOLUTIONS
  </div>
  <div class="photo" role="img" aria-label="Logistics collage: cargo plane over a world map, container ship and trucks with connected network icons" style="left:0;top:80px;width:342px;height:295px;background:linear-gradient(160deg,#c9dbe6 0%,#6f9bbd 35%,#2d5f8f 65%,#17324f 100%)"></div>
  <div class="abs" style="left:0;top:375px;width:342px;height:5px;background:var(--blue)"></div>
  <div class="abs company">COMPANY</div>
  <div class="abs profile">PROFILE</div>
  <div class="abs underline"></div>
  <div class="web" style="left:23px;top:461px">www.<b>tenhaul-solutions</b>.example</div>
</section>

<!-- Spread: company profile / mission / edge -->
<section class="page" style="left:452px;top:56px;width:342px;height:484px">
  <div class="photo" role="img" aria-label="Bright warehouse aisle with tall racks stacked with cardboard boxes" style="left:0;top:0;width:342px;height:128px;background:linear-gradient(100deg,#dfe6ee 0%,#b7c6d6 40%,#a38a63 75%,#8b7a60 100%)"></div>
  <div class="abs" style="left:17px;top:90px;font-size:14px;line-height:17px;font-weight:800;color:#fff">SHIPPING AND<br>LOGISTICS, PROJECT</div>
  <div class="heading" style="left:20px;top:138px;font-size:19px">COMPANY <span>PROFILE</span></div>
  <div class="rule" style="left:20px;top:165px;width:291px"><i style="width:68px"></i></div>
  <p class="copy" style="left:20px;top:172px;width:292px">A total logistics company covering domestic / international freight forwarding, warehouse management services, haulage, supply chain management, transport management &amp; distribution, procurement &amp; assembly services, shipping, chartering &amp; bunker services, project logistics &amp; tax exemption consultancy, oil &amp; gas logistics, halal logistics services &amp; integrated logistics management. We’re a well-established and experienced freight forwarder in Kuala Lumpur, Malaysia. We specialize in customized value-added solution that optimizes your supply chain by trimming inventory, reducing logistics cost and enhancing your customer service levels.</p>
  <p class="copy" style="left:20px;top:261px;width:292px">As a member of the Continental Parcel and Carriage Alliance which comprise of 170 global freight agents in 80 countries that promotes great handling in cross-trade logistics and freighting. You could rely on our efficiency in handlings of export cargo (FCL, LCL, Bulk and Conventional) between our global network offices worldwide with a total scale of 10,000 groomed specialists in various logistics division working together to ensure delivery task meets with your expectation. With our dedicated qualified and experienced professionals, we are fully committed to serving our clients.</p>
  <div class="abs blue" style="left:20px;top:335px;font-size:6.8px;font-weight:500">Our generic services are listed below for your reference:</div>
  <ul class="services" style="left:20px;top:346px;width:290px">
    <li>Air Freight</li>
    <li>Ocean Freight FCL &amp; LCL</li>
    <li>Container Haulage</li>
    <li>Warehousing</li>
    <li>Transportation and Distribution within Malaysia and Thailand</li>
    <li>Cross-Border Road Line-hauls between Thailand, Malaysia, Singapore and Laos</li>
    <li>Customs Brokerage and Forwarding</li>
    <li>Project Cargo Freight Forwarding for setting up of new plants / factories and ad hoc heavy-lift</li>
    <li>Air-Sea-Road-Rail multi-modal options</li>
    <li>Import / Export / Storage / Documentation / Handling of DG / Hazmat</li>
    <li>Vessel and Aircraft Charters</li>
  </ul>
  <div class="foot" style="left:10px"></div>
  <div class="pgno" style="left:10px">02</div>
</section>

<section class="page" style="left:794px;top:56px;width:343px;height:484px">
  <div class="heading" style="left:23px;top:18px;font-size:19px">OUR <span>MISSION</span></div>
  <div class="rule" style="left:23px;top:45px;width:291px"><i style="width:67px"></i></div>
  <p class="abs" style="left:23px;top:55px;width:275px;font-size:9.6px;line-height:12.6px;color:var(--text)">Based on the motto “Quick, Reliable and Polite”, we are dedicated to upholding the following three points corporate philosophy:</p>

  <div class="mission-box" style="left:21px">
    <svg class="badge" viewBox="0 0 42 46" aria-hidden="true"><polygon points="21,1 41,12 41,34 21,45 1,34 1,12" fill="#1c1d21" stroke="#fff" stroke-width="2"/></svg>
    <span class="badge"><b>01</b></span>
    Adhering To The Principle That “The Customer Always Comes First”.
  </div>
  <div class="mission-box" style="left:127px">
    <svg class="badge" viewBox="0 0 42 46" aria-hidden="true"><polygon points="21,1 41,12 41,34 21,45 1,34 1,12" fill="#1c1d21" stroke="#fff" stroke-width="2"/></svg>
    <span class="badge"><b>02</b></span>
    Contributing To The Development Of The Local Community.
  </div>
  <div class="mission-box" style="left:233px">
    <svg class="badge" viewBox="0 0 42 46" aria-hidden="true"><polygon points="21,1 41,12 41,34 21,45 1,34 1,12" fill="#1c1d21" stroke="#fff" stroke-width="2"/></svg>
    <span class="badge"><b>03</b></span>
    Making It Our Duty To Be Responsible And Sincere.
  </div>

  <div class="edge">
    <div class="heading" style="left:23px;top:12px;font-size:19px">OUR <span>EDGE</span></div>
    <div class="rule" style="left:23px;top:39px;width:291px;background:#5a5f68"><i style="width:67px"></i></div>

    <div class="edge-item" style="left:7px;top:57px"><svg viewBox="0 0 30 33"><polygon points="15,1 29,9 29,24 15,32 1,24 1,9" fill="#fff" stroke="var(--blue)" stroke-width="2"/><rect x="8" y="12" width="9" height="7" fill="var(--blue)"/><rect x="17" y="14" width="5" height="5" fill="var(--blue)"/><circle cx="11" cy="21" r="1.6" fill="var(--blue)"/><circle cx="19" cy="21" r="1.6" fill="var(--blue)"/></svg>One-Stop<br>Logistics<br>Solutions</div>
    <div class="edge-item" style="left:79px;top:57px"><svg viewBox="0 0 30 33"><polygon points="15,1 29,9 29,24 15,32 1,24 1,9" fill="#fff" stroke="var(--blue)" stroke-width="2"/><circle cx="15" cy="16.5" r="3" fill="var(--blue)"/><g stroke="var(--blue)" stroke-width="1.2"><line x1="15" y1="16.5" x2="9" y2="11"/><line x1="15" y1="16.5" x2="21" y2="11"/><line x1="15" y1="16.5" x2="9" y2="22"/><line x1="15" y1="16.5" x2="21" y2="22"/></g><circle cx="9" cy="11" r="1.8" fill="var(--blue)"/><circle cx="21" cy="11" r="1.8" fill="var(--blue)"/><circle cx="9" cy="22" r="1.8" fill="var(--blue)"/><circle cx="21" cy="22" r="1.8" fill="var(--blue)"/></svg>Extensive Network<br>Throughout<br>Malaysia</div>
    <div class="edge-item" style="left:160px;top:57px;width:94px"><svg viewBox="0 0 30 33"><polygon points="15,1 29,9 29,24 15,32 1,24 1,9" fill="#fff" stroke="var(--blue)" stroke-width="2"/><circle cx="15" cy="12" r="3.2" fill="var(--blue)"/><path d="M9 23c0-4 3-6 6-6s6 2 6 6z" fill="var(--blue)"/></svg>Highly Qualified<br>and Experienced<br>Pool of Professionals</div>
    <div class="edge-item" style="left:238px;top:57px"><svg viewBox="0 0 30 33"><polygon points="15,1 29,9 29,24 15,32 1,24 1,9" fill="#fff" stroke="var(--blue)" stroke-width="2"/><circle cx="15" cy="14" r="4.5" fill="none" stroke="var(--blue)" stroke-width="2.2" stroke-dasharray="2.2 1.4"/><circle cx="15" cy="14" r="1.6" fill="var(--blue)"/><path d="M8 22h14" stroke="var(--blue)" stroke-width="2"/></svg>Comprehensive<br>IT Solutions</div>

    <div class="edge-item" style="left:48px;top:129px;width:86px"><svg viewBox="0 0 30 33"><polygon points="15,1 29,9 29,24 15,32 1,24 1,9" fill="#fff" stroke="var(--blue)" stroke-width="2"/><circle cx="15" cy="16.5" r="6" fill="none" stroke="var(--blue)" stroke-width="1.8"/><circle cx="15" cy="16.5" r="2" fill="var(--blue)"/></svg>Innovative<br>and<br>Customer-focused<br>Solutions</div>
    <div class="edge-item" style="left:131px;top:129px"><svg viewBox="0 0 30 33"><polygon points="15,1 29,9 29,24 15,32 1,24 1,9" fill="#fff" stroke="var(--blue)" stroke-width="2"/><path d="M21 16.5a6 6 0 1 1-2-4.5" fill="none" stroke="var(--blue)" stroke-width="1.8"/><path d="M19 9v4h4" fill="none" stroke="var(--blue)" stroke-width="1.8"/><line x1="15" y1="13" x2="15" y2="17.5" stroke="var(--blue)" stroke-width="1.8"/><circle cx="15" cy="20" r="1" fill="var(--blue)"/></svg>Flexible<br>and Consistent<br>in Managing<br>Exceptions</div>
    <div class="edge-item" style="left:217px;top:129px"><svg viewBox="0 0 30 33"><polygon points="15,1 29,9 29,24 15,32 1,24 1,9" fill="#fff" stroke="var(--blue)" stroke-width="2"/><polygon points="15,9 21,12.5 21,20 15,23.5 9,20 9,12.5" fill="none" stroke="var(--blue)" stroke-width="1.8"/><circle cx="15" cy="16.5" r="2.2" fill="var(--blue)"/></svg>Total<br>Supply Chain<br>Visibility</div>
  </div>
  <div class="foot" style="right:10px"></div>
  <div class="pgno" style="right:10px">03</div>
</section>

<!-- Spread: target market / rules -->
<section class="page" style="left:56px;top:607px;width:342px;height:484px">
  <div class="sub" style="left:20px;top:20px">Target Market</div>
  <div class="rule" style="left:20px;top:40px;width:301px"><i style="width:80px"></i></div>
  <p class="small" style="left:20px;top:47px;width:300px"><span class="num" style="font-size:9px">1.</span> We sell the logistics services to all the industry in Malaysia and Worldwide.<br>&nbsp;&nbsp;&nbsp;&nbsp;(ONE Stop Logistics Solutions)</p>

  <div class="sub" style="left:20px;top:84px">Competitor</div>
  <div class="rule" style="left:20px;top:105px;width:301px"><i style="width:70px"></i></div>
  <div class="small" style="left:22px;top:112px;width:300px;height:40px">
    <span class="abs" style="left:0;top:0"><span class="dot">1</span> RT Vollmark</span>
    <span class="abs" style="left:107px;top:0"><span class="dot">2</span> Corventa Transport</span>
    <span class="abs" style="left:214px;top:0"><span class="dot">3</span> Brastow + Feld</span>
    <span class="abs" style="left:0;top:14px"><span class="dot">4</span> TOLRI</span>
    <span class="abs" style="left:107px;top:14px"><span class="dot">5</span> QVN</span>
    <span class="abs" style="left:214px;top:14px"><span class="dot">6</span> Trundelles</span>
    <span class="abs" style="left:0;top:28px"><span class="dot">7</span> Wiro Logistics</span>
  </div>

  <div class="photo" role="img" aria-label="Trucks on a highway with a hand holding a tablet and glowing network connection lines" style="left:0;top:164px;width:342px;height:193px;background:linear-gradient(135deg,#e8eef4 0%,#9fbcd6 35%,#4d7fae 70%,#2a4d72 100%)"></div>

  <div class="sub" style="left:20px;top:369px">Rules for Picking a Company Name</div>
  <div class="rule" style="left:20px;top:391px;width:301px"><i style="width:100px"></i></div>
  <div class="small" style="left:21px;top:398px;width:300px;height:40px">
    <span class="abs" style="left:0;top:0"><span class="num">1.</span> Unique and unforgettable</span>
    <span class="abs" style="left:0;top:14px"><span class="num">2.</span> Avoid unusual spellings</span>
    <span class="abs" style="left:0;top:28px"><span class="num">3.</span> Easy to pronounce and remember</span>
    <span class="abs" style="left:179px;top:0"><span class="num">4.</span> Keep it simple</span>
    <span class="abs" style="left:179px;top:14px"><span class="num">5.</span> Make some sense</span>
    <span class="abs" style="left:179px;top:28px"><span class="num">6.</span> Give a clue</span>
  </div>
  <div class="foot" style="left:10px"></div>
  <div class="pgno" style="left:10px">02</div>
</section>

<section class="page" style="left:398px;top:607px;width:342px;height:484px">
  <div class="photo" role="img" aria-label="Warehouse conveyor with pallet of boxes, a plane over a globe, and a hand holding a tablet with logistics icons" style="left:0;top:0;width:342px;height:292px;background:linear-gradient(160deg,#dbe6f1 0%,#8fb1d3 35%,#3f6e9f 65%,#1f2f45 100%)"></div>

  <div class="sub" style="left:19px;top:303px;line-height:13px"><span class="blue">Rules for Picking a</span><br>Company Logo</div>
  <div class="rule" style="left:19px;top:337px;width:136px"><i style="width:40px"></i></div>
  <ul class="numlist" style="left:19px;top:344px">
    <li><span class="dot">1</span> Unique and unforgettable</li>
    <li><span class="dot">2</span> Avoid unusual spellings</li>
    <li><span class="dot">3</span> Easy to pronounce and remember</li>
    <li><span class="dot">4</span> Keep it simple</li>
    <li><span class="dot">5</span> Make some sense</li>
    <li><span class="dot">6</span> Give a clue</li>
  </ul>

  <div class="sub" style="left:186px;top:303px;line-height:13px"><span class="blue">Rules for Picking a</span><br>Company Logo</div>
  <div class="rule" style="left:186px;top:337px;width:137px"><i style="width:40px"></i></div>
  <ul class="numlist" style="left:186px;top:343px">
    <li><span class="dot">1</span> Simplicity</li>
    <li><span class="dot">2</span> Memorability</li>
    <li><span class="dot">3</span> Originality</li>
    <li><span class="dot">4</span> Modern Yet Timeless</li>
    <li><span class="dot">5</span> Balance</li>
    <li><span class="dot">6</span> Complementary</li>
    <li><span class="dot">7</span> Versatility</li>
  </ul>
  <div class="foot" style="right:10px"></div>
  <div class="pgno" style="right:10px">03</div>
</section>

<!-- Back cover -->
<section class="page back" style="left:794px;top:607px;width:343px;height:484px">
  <div class="brand" style="left:113px;top:30px;font-size:11px;gap:6px">
    <span class="mark" style="width:10px;height:10px"></span>TENHAUL SOLUTIONS
  </div>
  <div class="title">Tenhaul Solutions Sdn. Bhd.</div>
  <div class="lined" style="top:84px">Registration : 2738516-P</div>
  <div class="photo" role="img" aria-label="Globe with a passenger plane, container ship, trucks and city skyline in warm and blue tones" style="left:0;top:100px;width:343px;height:246px;background:radial-gradient(circle at 55% 45%,#e9a283 0%,#c7cfe0 35%,#9fb6d0 60%,#eef2f6 100%)"></div>
  <div class="person">Derek Tan</div>
  <div class="lined" style="top:370px;font-size:9px">Manager</div>
  <div class="contact">
    Mobile No : (+6019) 4183907<br>
    Office No : (+607) 2918476<br>
    Email : derek.tan@tenhaul-solutions.example<br>
    <span style="display:block;margin-top:2px">42-07, Jalan Seri Dedap 5, Taman Bukit Kenari, 81100<br>Johor Bahru, Johor, Malaysia.</span>
  </div>
  <div class="web" style="left:0;right:0;top:458px;text-align:center;font-size:11px;font-weight:500">www.<b>tenhaul-solutions</b>.example</div>
</section>

</body>
</html>
```